Business Card cabinets and cabinets components making company.

the card should be formal and interesting at the same time. The main colors will be black and white.

Font styles to use
Sans Serif

Colors

Designer to choose only greyscale colors for use in the design.

Requirements
Must have
• At least must have the followings:
office phone
cell phone
address
position
name
email
web

```html
<!DOCTYPE html>
<html lang="en">
<head>
<meta charset="utf-8">
<title>Trimwell Business Card</title>
<link href="https://fonts.googleapis.com/css2?family=Poppins:wght@400;500;600&display=swap" rel="stylesheet">
<style>
  :root {
    --stage: #1e1e1e;
    --card-dark: #111111;
    --card-light: #fbfbfb;
    --ink: #111111;
    --ink-soft: #2a2a2a;
    --silver: #d8d8d8;
    --silver-dim: #6a6a6a;
  }
  * { margin: 0; padding: 0; box-sizing: border-box; }
  html, body {
    width: 1200px; height: 1200px; overflow: hidden;
    background: var(--stage);
    font-family: "Poppins", sans-serif;
  }
  .stage {
    width: 1200px; height: 1200px;
    display: flex; flex-direction: column; align-items: center; justify-content: center;
    gap: 48px;
  }
  .card {
    width: 860px; height: 491px; position: relative;
    box-shadow: 0 18px 40px rgba(0,0,0,0.55);
  }
  /* Back side */
  .card--back { background: var(--card-dark); }
  .brand-lockup {
    position: absolute; left: 0; right: 0; top: 190px;
    display: flex; justify-content: center; align-items: center; gap: 16px;
  }
  .brand-lockup__square {
    width: 30px; height: 30px; background: var(--silver);
  }
  .brand-lockup__name {
    font-weight: 600; font-size: 62px; color: var(--silver); letter-spacing: 0.5px;
  }
  .back-url {
    position: absolute; left: 0; right: 0; bottom: 52px; text-align: center;
    font-size: 16px; letter-spacing: 1.5px; color: var(--silver-dim);
  }
  /* Front side */
  .card--front { background: var(--card-light); color: var(--ink); }
  .front-brand {
    position: absolute; left: 70px; top: 0; bottom: 0; width: 290px;
    display: flex; flex-direction: column; justify-content: center; align-items: flex-start; gap: 18px;
  }
  .front-brand__square { width: 44px; height: 44px; background: var(--ink); }
  .front-brand__name { font-weight: 600; font-size: 58px; line-height: 1; color: var(--ink); }
  .details {
    position: absolute; left: 420px; top: 92px;
  }
  .details__name { font-weight: 600; font-size: 34px; line-height: 1.1; }
  .details__role { font-size: 20px; color: var(--ink-soft); margin-top: 2px; }
  .contact-list { list-style: none; margin-top: 30px; }
  .contact-list li {
    display: flex; align-items: center; gap: 18px;
    font-size: 22px; line-height: 1; height: 32px;
  }
  .icon {
    width: 24px; height: 24px; background: var(--ink); border-radius: 2px;
    display: flex; align-items: center; justify-content: center; flex: none;
  }
  .icon svg { width: 16px; height: 16px; }
  .address {
    display: flex; gap: 18px; margin-top: 22px;
    font-size: 22px; line-height: 1.3;
  }
  .address .icon { margin-top: 2px; }
</style>
</head>
<body>
<main class="stage">
  <section class="card card--back">
    <div class="brand-lockup">
      <span class="brand-lockup__square"></span>
      <span class="brand-lockup__name">Trimwell</span>
    </div>
    <p class="back-url">www.trimwell.com</p>
  </section>

  <section class="card card--front">
    <div class="front-brand">
      <span class="front-brand__square"></span>
      <span class="front-brand__name">Trimwell</span>
    </div>
    <div class="details">
      <h1 class="details__name">Daniel Reyes</h1>
      <p class="details__role">Managing Director</p>
      <ul class="contact-list">
        <li><span class="icon"><svg viewBox="0 0 16 16"><path fill="#fff" d="M3 1.5h3l1 3.5-2 1.3a8 8 0 0 0 4.7 4.7L11 9l3.5 1v3c0 .8-.7 1.5-1.5 1.5C7 14.5 1.5 9 1.5 3c0-.8.7-1.5 1.5-1.5z"/></svg></span>312 555 0148</li>
        <li><span class="icon"><svg viewBox="0 0 16 16"><rect x="4" y="1" width="8" height="14" rx="1.5" fill="#fff"/><rect x="5.5" y="3" width="5" height="8" fill="#111"/></svg></span>312 555 0148</li>
        <li><span class="icon"><svg viewBox="0 0 16 16"><rect x="1.5" y="3.5" width="13" height="9" fill="none" stroke="#fff" stroke-width="1.4"/><path d="M1.5 3.5 8 9l6.5-5.5" fill="none" stroke="#fff" stroke-width="1.4"/></svg></span>hello@trimwell.com</li>
        <li><span class="icon"><svg viewBox="0 0 16 16" fill="none" stroke="#fff" stroke-width="1.2"><circle cx="8" cy="8" r="6.3"/><ellipse cx="8" cy="8" rx="2.8" ry="6.3"/><path d="M1.7 8h12.6M2.8 4.8h10.4M2.8 11.2h10.4"/></svg></span>www.trimwell.com</li>
      </ul>
      <div class="address">
        <span class="icon"><svg viewBox="0 0 16 16"><path fill="#fff" d="M8 1a5 5 0 0 0-5 5c0 3.5 5 9 5 9s5-5.5 5-9a5 5 0 0 0-5-5z"/><circle cx="8" cy="6" r="1.8" fill="#111"/></svg></span>
        <p>118 Alder Street<br>Suite 210, Fairview<br>MI 49000</p>
      </div>
    </div>
  </section>
</main>
</body>
</html>
```